Poster Design Project - Front Window Poster for IT Business

Design a poster to be displayed in the front window of our office.
To include the following text:
Proactive Network Solutions
Servers & Networks
Workly 480
Cloud Solutions
Helpdesk Services & Support
Network Audits
Disaster Recovery
IT Consulting
Contact details to be shown on the poster:
www.qe.com.au
02 5550 1824
Please also include the logo and related colour scheme.
Needs to look professional and easy to read from the street.
Must be in A1 format, printable through quillomark.
Hi Designers,
Nadia

```html
<!DOCTYPE html>
<html lang="en">
<head>
<meta charset="utf-8">
<title>Peace of Mind – QE Technology Solutions</title>
<link rel="stylesheet" href="https://fonts.googleapis.com/css2?family=Cormorant+Garamond:wght@500&family=PT+Sans+Narrow:wght@400&display=swap">
<style>
  :root {
    --forest-deep: #123f3d;
    --forest-mid: #2f6f6a;
    --water-light: #a9cdd6;
    --figure-haze: #bfe0ea;
    --panel: rgba(236, 242, 246, 0.72);
    --panel-fade: rgba(228, 238, 242, 0);
    --headline-blue: #1b3fae;
    --list-blue: #2d68df;
    --contact-blue: #1f5fd6;
  }
  * { margin: 0; padding: 0; box-sizing: border-box; }
  html, body { width: 1200px; height: 854px; overflow: hidden; background: #ffffff; }
  .poster {
    position: relative;
    width: 1200px;
    height: 854px;
    overflow: hidden;
  }
  .backdrop-photo {
    position: absolute;
    inset: 0;
    background:
      radial-gradient(ellipse 300px 420px at 330px 500px, var(--figure-haze) 0%, rgba(191,224,234,0) 100%),
      radial-gradient(ellipse 520px 360px at 880px 600px, var(--water-light) 0%, rgba(169,205,214,0) 70%),
      linear-gradient(160deg, var(--forest-deep) 0%, var(--forest-mid) 50%, #4f8c8a 75%, #24504f 100%);
  }
  .info-panel {
    position: absolute;
    left: 430px;
    top: 97px;
    width: 705px;
    height: 703px;
    background: linear-gradient(90deg, var(--panel-fade) 0%, var(--panel) 25%, var(--panel) 100%);
  }
  .content {
    position: absolute;
    left: 660px;
    top: 0;
    width: 474px;
    text-align: center;
  }
  .headline {
    position: absolute;
    left: 0; width: 100%;
    top: 166px;
    font-family: "Cormorant Garamond", "Times New Roman", serif;
    font-weight: 500;
    font-size: 62px;
    line-height: 1;
    color: var(--headline-blue);
  }
  .services {
    position: absolute;
    left: 0; width: 100%;
    top: 284px;
    list-style: none;
    font-family: "PT Sans Narrow", "Arial Narrow", sans-serif;
    font-size: 28px;
    line-height: 40.3px;
    color: var(--list-blue);
  }
  .brand {
    position: absolute;
    left: 0; width: 100%;
    top: 662px;
    display: flex;
    align-items: center;
    justify-content: center;
    gap: 10px;
    font-family: "PT Sans Narrow", "Arial Narrow", sans-serif;
    font-size: 30px;
    line-height: 1;
    color: var(--list-blue);
  }
  .brand-mark {
    width: 18px;
    height: 18px;
    background: var(--list-blue);
  }
  .contact {
    position: absolute;
    left: 0; width: 100%;
    top: 716px;
    font-family: "PT Sans Narrow", "Arial Narrow", sans-serif;
    font-size: 23px;
    line-height: 31px;
    color: var(--contact-blue);
  }
</style>
</head>
<body>
  <main class="poster">
    <div class="backdrop-photo" role="img" aria-label="Woman in pale blue clothing meditating cross-legged on a wooden jetty beside a blurred forest lake"></div>
    <div class="info-panel"></div>

    <section class="content">
      <h1 class="headline">Peace of Mind</h1>
      <ul class="services">
        <li>Proactive Network Solutions</li>
        <li>Servers &amp; Networks</li>
        <li>Workly 480</li>
        <li>Cloud Solutions</li>
        <li>Helpdesk Services &amp; Support</li>
        <li>Network Audits</li>
        <li>Disaster Recovery</li>
        <li>IT Consulting</li>
      </ul>
      <div class="brand"><span class="brand-mark"></span><span>QE Technology Solutions</span></div>
      <p class="contact">www.qe.com.au<br>02 5550 1824</p>
    </section>
  </main>
</body>
</html>
```